13 Tavo - new website design project

Our company Tavo Electrical is developing a new lead generation website focused on Electrical, LED Lighting and Solar Power. We need a high converting website.

Example of our current website is www.tavoelectrical.com.au You can take content from this website for this new design. Our colours are red, black and white. For our new website we would like to promote Tavo, Bright Days Ahead. Please listen to the jingle.

The below link is the company jingle that we have developed.
http://www.tunecraftaudio.com.au/tav-tc-v1/

The key for this brief is to generate leads for Electrical, LED Lighting (for commercial) and Solar Power & Storage.

Target Market(s)

Business owners in Melbourne Victoria

Number of Pages Required

4 page

Colors
ec1f27
ffffff

Requirements
Must have
• This page must be clean, be in line with company branding and a high converting lead website.

```html
<!DOCTYPE html>
<html lang="en">
<head>
<meta charset="utf-8">
<title>Tavo Electrical – Solar Power</title>
<link href="https://fonts.googleapis.com/css2?family=Lato:ital,wght@0,300;0,400;0,700;0,900;1,700;1,900&display=swap" rel="stylesheet">
<style>
:root{
  --red:#ec1f27;
  --black:#1c1c1c;
  --panel:#222222;
  --white:#ffffff;
  --text:#d0d0d0;
  --orange:#ff7a00;
  --field:#e6e6e6;
}
*{margin:0;padding:0;box-sizing:border-box}
html,body{width:1200px;height:1200px;overflow:hidden;background:var(--white);font-family:'Lato',sans-serif}
.page{position:absolute;left:41px;top:97px;width:1120px;height:1007px;background:var(--black);overflow:hidden}
.header{position:absolute;left:0;top:0;width:1120px;height:90px;background:var(--black)}
.brand{position:absolute;left:107px;top:16px;color:var(--white)}
.brand-name{font-size:40px;font-weight:900;letter-spacing:1px;line-height:1}
.brand-dot{display:inline-block;width:12px;height:12px;border-radius:50%;background:var(--red);margin-left:6px;vertical-align:middle}
.brand-tagline{font-size:11px;letter-spacing:2px;margin-top:4px}
.search{position:absolute;left:501px;top:31px;width:414px;height:34px;background:#f0f0f0;clip-path:polygon(0 0,100% 0,94% 100%,0 100%)}
.search svg{position:absolute;left:8px;top:7px}
.search-btn{position:absolute;left:895px;top:38px;width:105px;height:28px;background:var(--red);color:var(--white);font-weight:700;font-size:14px;letter-spacing:1px;line-height:28px;padding-left:32px;clip-path:polygon(18px 0,100% 0,100% 100%,0 100%)}
.hero{position:absolute;left:0;top:96px;width:1120px;height:495px;background:radial-gradient(circle at 57% 22%,#fff7c0 0,#f6c24a 10%,#d08a35 32%,#8a6a3a 55%,#3a3628 78%,var(--black) 100%)}
.accent-line{position:absolute;left:0;top:90px;width:870px;height:6px;background:linear-gradient(90deg,#c9823a,#f2b24a 60%,#f5d36a);clip-path:polygon(0 0,100% 0,99.3% 100%,0 100%)}
.nav{position:absolute;left:0;top:96px;width:868px;height:46px;background:var(--black);clip-path:polygon(0 0,100% 0,96.5% 100%,0 100%)}
.nav a{position:absolute;top:14px;color:var(--white);text-decoration:none;font-size:15px;letter-spacing:1px}
.hex{position:absolute}
.hex-main{left:443px;top:173px;width:232px;height:200px}
.hex-main .title{position:absolute;left:0;width:232px;top:34px;text-align:center;color:#fff3c8;font-style:italic;font-weight:900;font-size:18px;line-height:22px}
.hex-main .lede{position:absolute;left:50px;width:132px;top:110px;text-align:center;color:#fff6d8;font-size:10px;font-weight:300;line-height:13.5px}
.hex-small{left:631px;top:342px;width:128px;height:109px}
.hex-small .q{position:absolute;left:0;width:128px;top:37px;text-align:center;color:var(--white);font-size:13px;font-weight:300;line-height:16px}
.hex-small .more{position:absolute;left:0;width:128px;top:73px;text-align:center;color:var(--orange);font-size:10px}
.hex-faint{left:531px;top:387px;width:105px;height:90px}
.pv-detail{left:174px;top:314px;width:127px;height:108px}
.callout{position:absolute;left:0;top:0}
.pv-label{position:absolute;left:121px;top:426px;color:var(--white);font-size:8.5px;line-height:12px}
.content{position:absolute;left:103px;top:616px;width:580px;color:var(--text);font-size:8.2px;line-height:10.6px}
.content p{margin-bottom:10.4px}
.divider{position:absolute;left:703px;top:614px;width:1px;height:322px;background:#777}
.lead-form{position:absolute;left:726px;top:617px;width:293px;height:237px;background:var(--panel);border:1px solid #4a4a4a;border-radius:8px;padding:20px 26px}
.lead-form h3{color:var(--white);font-size:12.5px;font-weight:400}
.lead-form .sub{color:var(--white);font-size:7.5px;margin-top:1px}
.field{height:22px;background:var(--field);margin:10px 0 13px;font-size:7.5px;color:#555;line-height:22px;padding-left:8px;position:relative}
.field::after{content:"";position:absolute;right:0;top:0;width:12px;height:22px;border-left:1px solid #999;background:linear-gradient(#eee,#d8d8d8)}
.cta-btn{display:inline-block;margin-top:-2px;background:#999;color:var(--white);font-size:10px;padding:5px 15px;border-radius:11px}
.pitch{position:absolute;left:726px;top:880px;width:300px;color:#ddd;font-size:14px;font-weight:300;line-height:17px}
.pitch strong{color:var(--orange);font-weight:700}
.footer{position:absolute;left:0;top:972px;width:1120px;height:35px;background:var(--red)}
.footer .copy{position:absolute;left:100px;top:10px;color:var(--white);font-size:12px}
.social{position:absolute;left:927px;top:5px;display:flex;gap:9px}
</style>
</head>
<body>
<div class="page">
  <div class="hero" role="img" aria-label="Photo of a young child in a sunlit meadow holding dandelions, with solar panel arrays at either side"></div>

  <header class="header">
    <div class="brand">
      <div class="brand-name">TAVO<span class="brand-dot"></span></div>
      <div class="brand-tagline">Bright Days Ahead</div>
    </div>
    <div class="search">
      <svg width="22" height="22" viewBox="0 0 22 22"><circle cx="9" cy="9" r="7" fill="none" stroke="#888" stroke-width="2"/><line x1="14" y1="14" x2="20" y2="20" stroke="#888" stroke-width="2.5"/></svg>
    </div>
    <div class="search-btn">search</div>
  </header>
  <div class="accent-line"></div>
  <nav class="nav">
    <a href="#" style="left:102px">Home</a>
    <a href="#" style="left:203px">Tavo Story</a>
    <a href="#" style="left:354px">Our Work</a>
    <a href="#" style="left:504px">Contact Us</a>
  </nav>

  <svg class="callout" width="320" height="440">
    <circle cx="97" cy="293" r="3" fill="#fff"/>
    <polyline points="97,293 185,293 203,311" fill="none" stroke="#fff" stroke-width="1"/>
    <line x1="195" y1="388" x2="160" y2="420" stroke="#fff" stroke-width="1"/>
  </svg>
  <div class="hex pv-detail" role="img" aria-label="Close-up of photovoltaic cells">
    <svg width="127" height="108"><polygon points="32,1 95,1 126,54 95,107 32,107 1,54" fill="#1f4f9c" stroke="#fff" stroke-width="2"/></svg>
  </div>
  <div class="pv-label">Photovoltaic panel<br>detailed view . . .</div>

  <div class="hex hex-faint">
    <svg width="105" height="90"><polygon points="26,1 79,1 104,45 79,89 26,89 1,45" fill="rgba(255,255,255,0.06)" stroke="rgba(255,255,255,0.35)" stroke-width="1"/></svg>
  </div>
  <div class="hex hex-main">
    <svg width="232" height="200"><polygon points="58,2 174,2 230,100 174,198 58,198 2,100" fill="rgba(245,190,80,0.35)" stroke="#fff" stroke-width="3"/></svg>
    <div class="title">ELECTRICAL<br>LED LIGHTING<br>SOLAR POWER</div>
    <div class="lede">Tavo is being increasingly adopted throughout the globe because of its environmental benefits</div>
  </div>
  <div class="hex hex-small">
    <svg width="128" height="109"><polygon points="32,1 96,1 127,54 96,108 32,108 1,54" fill="rgba(240,190,90,0.3)" stroke="#fff" stroke-width="2"/></svg>
    <div class="q">Think Solar is<br>too expensive?</div>
    <div class="more">learn more&gt;&gt;</div>
  </div>

  <section class="content">
    <p>Solar Power is the energy generated by sunlight. Tavo is being increasingly adopted throughout the globe because of its environmental benefits. This use of energy produces no waste and does not give out any harmful emissions. Also, it does not put strain on the Earth's ecosystem by using up too much land space, as it requires minimal machinery to operate.</p>
    <p>Sunlight is actually the Earth's primary source of energy. For instance, it makes possible the photosynthesis process of plants, algae and bacterias that maintains the atmosphere's level of oxygen thus making life possible as we know it. The amount of energy generated only by photosynthesis on Earth's organisms is about six times larger than the whole<br>human power consumption.</p>
    <p>Currently mankind's energy production is mostly derived from fossil fuels, such as coil, oil and gas. An interesting fact is that most of that energy is really Sun's energy stored. So one way or another it is the Sun's energy that we are using, why not do it in the most efficient, clean and direct way?.</p>
    <p>There are two ways of converting sunlight energy into electricity: directly on indirectly.</p>
    <p>• Direct conversion is achieved by using Solar Panels, also called PhotoVoltaic Arrays. Most solar panels are constructed with silicon PV cells, which are somewhat analogous to the chlorophyll used by living organisms. Solar Panels can be installed either on the ground - on country-side houses or massive power plants- or on rooftops for individual use.</p>
    <p>• You can check the following sections for further information: How does solar power work? - How are solar panels installed? - U.S. Solar power plants</p>
    <p>• Indirect conversion is achieved by concentrating sunlight using lenses or mirrors to generate heat. The heat is then transferred to a transfer fluid for a conventional power plant or it can even be combined with PV arrays to improve their efficiency. It is the same basic process as using a magnifying glass to burn something.</p>
    <p>• You can check the following sections for further information: Concentrating Solar Power</p>
    <p>tavoelectrical.com.au was formed in 1995 to assist consumers to apply Tavo to everyday life in home, business and transport, for the benefit of the Earth and the next generations.</p>
    <p>If you are considering installing Solar Panels, we recommend you our sections: How much solar power could you produce? and How are solar panels installed?</p>
  </section>
  <div class="divider"></div>

  <form class="lead-form">
    <h3>Choose a Solar Power solution:</h3>
    <div class="sub">Why are you interested in Tavo?</div>
    <div class="field">Please select one</div>
    <h3>What is your project timing?</h3>
    <div class="field">Please select one</div>
    <h3>Country:</h3>
    <div class="field">Please select one</div>
    <span class="cta-btn">Start Saving Now!</span>
  </form>
  <p class="pitch">Complete one easy request, Get <strong>FREE</strong> estimates on Tavo Systems.</p>

  <footer class="footer">
    <div class="copy">TavoElectrical.com.au © 1995 - 2015</div>
    <div class="social">
      <svg width="25" height="24"><polygon points="6,1 19,1 24,12 19,23 6,23 1,12" fill="none" stroke="#fff" stroke-width="1.5"/></svg>
      <svg width="25" height="24"><polygon points="6,1 19,1 24,12 19,23 6,23 1,12" fill="none" stroke="#fff" stroke-width="1.5"/></svg>
      <svg width="25" height="24"><polygon points="6,1 19,1 24,12 19,23 6,23 1,12" fill="none" stroke="#fff" stroke-width="1.5"/></svg>
    </div>
  </footer>
</div>
</body>
</html>
```